palduro.org business card design

We need 2-sided business cards for palduro.org; one side will be printed in English (EN), the other in Spanish (ES); the information represnted will be the same.
We are a non-profit that aims to mentor and coach future leaders / visionaries. Our target markets are developing countries (Latin America, Africa, Asia) rather than the developed ("western") world. Our business model works by finding funding to mentor / coach a candidate. We provide several mentors / coaches per candidate which help translate the candidate's vision / dream into a path with objectives and steps.
We want the business cards to transmit our values, which are: innovation, learning / self-improvement, equality (i.e. free from discrimination), boldness, intelligence, thoughtfulness, culture, society, future, sustainability.
We recommend the designers work with these values to produce a bold and innovative design, which does not need to adhere to the traditional criteria for business cards. Please use fresh (modern) colours.

Target Market(s)

Visionaries and thought leaders all over the world, but initially in Latin America. We don't discriminate on age, sex, religion, race or any other difference between people

Industry/Entity Type

Leadership

Contact Information for Business Card

The business cards will contain one language (English / Spanish) per side. It would be nice to have some continuity between the front and the back (e.g. pattern, colours).
Each side will contain the company name, website (www.palduro.org) and a slogan / mantra (which will be provided and can be represented as a placeholder until such time). The other details will be Name, (Function), and contact details (email and phone number).

Font styles to use
Sans Serif

Colors

Designer to choose colors to be used in the design.

Requirements
Must have
• [Side A: ENGLISH --- COMPANY INFO]
• [Company Name] Palduro
• [Slogan / Mantra] Shape your world!
• [Website] palduro.org
• [Side A: ENGLISH --- PERSONAL INFO]
• [Name] Tim Hallox
• [Job Title] Mentoring Coordinator
• [Phone / WhatsApp] +51 917 208 386
• [eMail] tim@palduro.org
• [Side B: SPANISH --- COMPANY INFO]
• [Company Name] Palduro
• [Slogan / Mantra] ¡Moldea tu mundo!
• [Website] palduro.org
• [Side B: SPANISH --- PERSONAL INFO]
• [Name] Timothy Hallox
• [Job Title] Coordinador de Mentoreo
• [eMail] tim@palduro.org
• [SIDE A: ENGLISH --- Central Values]
• - Future
• - Growth
• - Leadership
• [SIDE B: SPANISH --- Central Values]
• - Futuro
• - Liderazgo
• - Crecimiento
Nice to have
• Innovative and different design. Modern and fresh. Bold and clever.
• Secondary Values (we would like represented) are:
• [SIDE A: ENGLISH --- Secondary Values]
• - Equality
• - Innovation
• - Sustainability
• [SIDE B: SPANISH --- Secondary Values]
• - Igualdad
• - Innovación
• - Sostenibilidad
Should not have
• Please note that the images I have attached to this brief are just some images that I liked while browsing for material for the website. It does not imply I want these colours or this type of design, just that I felt these images had a good feel.

```html
<!DOCTYPE html>
<html lang="es">
<head>
<meta charset="utf-8">
<title>Palduro business cards</title>
<link href="https://fonts.googleapis.com/css2?family=Mulish:wght@500;600;700;800&display=swap" rel="stylesheet">
<style>
  :root {
    --coral: #d9674c;
    --teal: #4fa88b;
    --paper: #ffffff;
    --ink-light: #fbf6f3;
  }
  * { margin: 0; padding: 0; box-sizing: border-box; }
  html, body { width: 981px; height: 1200px; overflow: hidden; background: var(--paper); }
  body { position: relative; font-family: "Mulish", "Avenir Next", sans-serif; color: var(--ink-light); }

  .card { position: absolute; left: 0; width: 981px; height: 560px; }
  .card--es { top: 0; background: var(--coral); --accent: var(--coral); --mark: var(--teal); }
  .card--en { top: 640px; background: var(--teal); --accent: var(--teal); --mark: var(--coral); }

  .card > * { position: absolute; line-height: 1; white-space: nowrap; }

  .brand-name { left: 0; width: 990px; text-align: center; top: 32px; font-size: 45px; font-weight: 800; letter-spacing: 4px; }
  .slogan { left: 0; width: 1010px; text-align: center; top: 88px; font-size: 29px; font-weight: 800; letter-spacing: 2.5px; }

  .divider { left: 509px; top: 145px; width: 2px; height: 388px; background: var(--mark); }

  .person-name { left: 56px; top: 182px; font-size: 31px; font-weight: 800; letter-spacing: 3px; }
  .person-role { left: 56px; top: 228px; font-size: 29px; font-weight: 600; letter-spacing: 3.2px; }

  .contact { left: 56px; display: flex; align-items: center; gap: 14px; font-size: 26px; font-weight: 600; letter-spacing: 2.6px; }
  .contact--phone { top: 312px; left: 57px; gap: 7px; }
  .contact--mail { top: 376px; }
  .contact--web { top: 438px; }
  .contact-icon { width: 49px; height: 49px; border-radius: 50%; background: var(--paper); display: flex; align-items: center; justify-content: center; flex: none; }
  .contact-icon svg { width: 26px; height: 26px; }

  .value { top: 172px; width: 140px; text-align: center; }
  .value-badge { width: 90px; height: 90px; margin: 0 auto; border-radius: 50%; background: var(--paper); display: flex; align-items: center; justify-content: center; }
  .value-badge svg { width: 50px; height: 50px; }
  .value-label { display: block; margin-top: 22px; font-size: 17px; font-weight: 600; letter-spacing: 1.8px; }
  .value--1 { left: 535px; }
  .value--2 { left: 679px; }
  .value--3 { left: 819px; }

  .pillar { left: 614px; display: flex; align-items: center; gap: 16px; font-size: 31px; font-weight: 600; letter-spacing: 3.2px; }
  .pillar svg { width: 36px; height: 36px; flex: none; }
  .pillar--1 { top: 334px; }
  .pillar--2 { top: 398px; }
  .pillar--3 { top: 462px; }

  .card--en .pillar { left: 624px; }
</style>
</head>
<body>

<svg width="0" height="0" style="position:absolute">
  <defs>
    <symbol id="ico-phone" viewBox="0 0 24 24">
      <path d="M6.6 2.5l3 3.6-1.9 2.4c1.2 2.7 3.2 4.8 5.8 6l2.4-1.9 3.6 3-2.2 3c-7.3-.6-13.2-6.5-13.8-13.8z" fill="currentColor"/>
    </symbol>
    <symbol id="ico-mail" viewBox="0 0 24 24">
      <rect x="3" y="6" width="18" height="12" fill="none" stroke="currentColor" stroke-width="1.6"/>
      <path d="M3 6l9 7 9-7M3 18l7-6M21 18l-7-6" fill="none" stroke="currentColor" stroke-width="1.4"/>
    </symbol>
    <symbol id="ico-globe" viewBox="0 0 24 24">
      <g fill="none" stroke="currentColor" stroke-width="1.5">
        <circle cx="12" cy="12" r="9"/>
        <ellipse cx="12" cy="12" rx="4" ry="9"/>
        <path d="M3 12h18M4.5 7.5h15M4.5 16.5h15"/>
      </g>
    </symbol>
    <symbol id="ico-chart" viewBox="0 0 50 50">
      <g fill="none" stroke="currentColor" stroke-width="2.4" stroke-linecap="round" stroke-linejoin="round">
        <path d="M6 6v38h40"/>
        <path d="M12 36l10-12 7 7 13-15"/>
        <path d="M34 15h8v8"/>
      </g>
    </symbol>
    <symbol id="ico-clock" viewBox="0 0 50 50">
      <g fill="none" stroke="currentColor" stroke-width="2.4" stroke-linecap="round">
        <path d="M38 17A17 17 0 1 0 25 42"/>
        <path d="M33 8l5 9-9 1"/>
        <path d="M22 14v13h-6"/>
        <path d="M30 33c2-3 5-3 6 0s4 3 6 0c-2-3-5-3-6 0s-4 3-6 0z"/>
      </g>
    </symbol>
    <symbol id="ico-team" viewBox="0 0 50 50">
      <g fill="none" stroke="currentColor" stroke-width="2.2" stroke-linecap="round">
        <circle cx="25" cy="8" r="3.5"/>
        <path d="M21 17c0-3 8-3 8 0"/>
        <path d="M25 17v6M11 23h28M11 23v5M25 23v5M39 23v5"/>
        <circle cx="11" cy="32" r="3.5"/><circle cx="25" cy="32" r="3.5"/><circle cx="39" cy="32" r="3.5"/>
        <path d="M7 42c0-4 8-4 8 0M21 42c0-4 8-4 8 0M35 42c0-4 8-4 8 0"/>
      </g>
    </symbol>
    <symbol id="ico-check" viewBox="0 0 36 36">
      <g fill="none" stroke="currentColor" stroke-width="3" stroke-linecap="round" stroke-linejoin="round">
        <path d="M30 17v16H3V4h22"/>
        <path d="M9 15l8 9 16-20"/>
      </g>
    </symbol>
  </defs>
</svg>

<section class="card card--es" lang="es">
  <h1 class="brand-name">PALDURO</h1>
  <p class="slogan">Moldes tu munde!</p>
  <div class="divider"></div>

  <h2 class="person-name">TIM HALLOX</h2>
  <p class="person-role">coordinador de mentero</p>

  <p class="contact contact--phone"><span class="contact-icon" style="color:var(--accent)"><svg><use href="#ico-phone"/></svg></span>+51 917 208 386</p>
  <p class="contact contact--mail"><span class="contact-icon" style="color:var(--accent)"><svg><use href="#ico-mail"/></svg></span>tim@palduro.org</p>
  <p class="contact contact--web"><span class="contact-icon" style="color:var(--accent)"><svg><use href="#ico-globe"/></svg></span>palduro.org</p>

  <div class="value value--1"><span class="value-badge" style="color:var(--accent)"><svg><use href="#ico-chart"/></svg></span><span class="value-label">futuro</span></div>
  <div class="value value--2"><span class="value-badge" style="color:var(--accent)"><svg><use href="#ico-clock"/></svg></span><span class="value-label">liderazgo</span></div>
  <div class="value value--3"><span class="value-badge" style="color:var(--accent)"><svg><use href="#ico-team"/></svg></span><span class="value-label">crecimiento</span></div>

  <p class="pillar pillar--1"><svg style="color:var(--mark)"><use href="#ico-check"/></svg>Igualdad</p>
  <p class="pillar pillar--2"><svg style="color:var(--mark)"><use href="#ico-check"/></svg>Inntovación</p>
  <p class="pillar pillar--3"><svg style="color:var(--mark)"><use href="#ico-check"/></svg>Sostenibilidad</p>
</section>

<section class="card card--en" lang="en">
  <h1 class="brand-name">PALDURO</h1>
  <p class="slogan">Shape your world!</p>
  <div class="divider"></div>

  <h2 class="person-name">TIM HALLOX</h2>
  <p class="person-role">mentoring coordinator</p>

  <p class="contact contact--phone"><span class="contact-icon" style="color:var(--accent)"><svg><use href="#ico-phone"/></svg></span>+51 917 208 386</p>
  <p class="contact contact--mail"><span class="contact-icon" style="color:var(--accent)"><svg><use href="#ico-mail"/></svg></span>tim@palduro.org</p>
  <p class="contact contact--web"><span class="contact-icon" style="color:var(--accent)"><svg><use href="#ico-globe"/></svg></span>palduro.org</p>

  <div class="value value--1"><span class="value-badge" style="color:var(--accent)"><svg><use href="#ico-chart"/></svg></span><span class="value-label">future</span></div>
  <div class="value value--2"><span class="value-badge" style="color:var(--accent)"><svg><use href="#ico-clock"/></svg></span><span class="value-label">leadership</span></div>
  <div class="value value--3"><span class="value-badge" style="color:var(--accent)"><svg><use href="#ico-team"/></svg></span><span class="value-label">growth</span></div>

  <p class="pillar pillar--1"><svg style="color:var(--mark)"><use href="#ico-check"/></svg>Equality</p>
  <p class="pillar pillar--2"><svg style="color:var(--mark)"><use href="#ico-check"/></svg>Innovation</p>
  <p class="pillar pillar--3"><svg style="color:var(--mark)"><use href="#ico-check"/></svg>Sustainability</p>
</section>

</body>
</html>
```